Screen design for customizable church app

I am building a customizable app for churches. I need the following screens designed:
1) Landing Screen
-- Text field to enter a code to join a organization
-- Button to register a new organization
2) Registration Screen
-- Text field to enter an organization name
-- Register button
-- Screen should indicate price/month and free trial for X days
3) Restricted (requires login) screen
4) Organization home screen
-- Dynamic menu options of the following types:
a) Contact Us/Form
b) Video List
c) Audio List
d) Documents List
e) Message/Chat Rooms
f) Map/Directions
g) Webpage

Plus permission based options:
h) Profile Settings
i) Notification Center
j) Admin Settings
k) Manage members
l) View Form Submissions

Low-fi/wireframe designs attached. No color scheme or branding has been established yet.

```html
<!DOCTYPE html>
<html lang="en">
<head>
<meta charset="utf-8">
<title>Chapel Wave – Home</title>
<link rel="stylesheet" href="https://fonts.googleapis.com/css2?family=Poppins:wght@300;400;500&display=swap">
<style>
  :root {
    --header-top: #2d5aa0;
    --header-bottom: #1d3a6c;
    --header-text: #ffffff;
    --icon-stroke: #1c3d6b;
    --label: #6b6b6b;
    --accent-gold: #b08a4c;
    --page: #ffffff;
  }
  * { box-sizing: border-box; margin: 0; padding: 0; }
  html, body {
    width: 676px;
    height: 1200px;
    overflow: hidden;
    background: var(--page);
    font-family: "Poppins", sans-serif;
  }
  .app-screen {
    position: relative;
    width: 676px;
    height: 1200px;
  }
  .app-header {
    position: absolute;
    top: 0; left: 0;
    width: 100%;
    height: 106px;
    background: linear-gradient(180deg, var(--header-top), var(--header-bottom));
    display: flex;
    align-items: center;
    justify-content: center;
  }
  .app-title {
    color: var(--header-text);
    font-weight: 500;
    font-size: 30px;
    letter-spacing: 0.2px;
  }
  .menu-toggle {
    position: absolute;
    right: 33px;
    top: 32px;
    width: 42px;
    height: 42px;
  }
  .menu-grid {
    position: absolute;
    top: 272px;
    left: 35px;
    display: grid;
    grid-template-columns: repeat(3, 202px);
    grid-template-rows: 178px 186px 188px 186px;
  }
  .menu-item {
    display: flex;
    flex-direction: column;
    align-items: center;
  }
  .menu-icon {
    width: 64px;
    height: 64px;
    fill: none;
    stroke: var(--icon-stroke);
    stroke-width: 3;
    stroke-linecap: round;
    stroke-linejoin: round;
  }
  .menu-label {
    margin-top: 20px;
    color: var(--label);
    font-weight: 300;
    font-size: 20px;
    line-height: 21px;
    text-align: center;
  }
  .menu-item.is-active .menu-icon { stroke: url(#goldStroke); }
  .menu-item.is-active .menu-label { color: var(--accent-gold); }
  .icon-defs { position: absolute; width: 0; height: 0; }
</style>
</head>
<body>
<svg class="icon-defs" aria-hidden="true">
  <defs>
    <linearGradient id="goldStroke" gradientUnits="userSpaceOnUse" x1="0" y1="0" x2="64" y2="64">
      <stop offset="0" stop-color="#d6b16e"/>
      <stop offset="1" stop-color="#a57f3f"/>
    </linearGradient>
    <symbol id="gear" viewBox="0 0 64 64">
      <polygon points="25.93,10.86 27.14,4.42 36.86,4.42 38.07,10.86 42.67,12.75 48.07,9.07 54.93,15.93 51.25,21.33 53.14,25.93 59.58,27.14 59.58,36.86 53.14,38.07 51.25,42.67 54.93,48.07 48.07,54.93 42.67,51.25 38.07,53.14 36.86,59.58 27.14,59.58 25.93,53.14 21.33,51.25 15.93,54.93 9.07,48.07 12.75,42.67 10.86,38.07 4.42,36.86 4.42,27.14 10.86,25.93 12.75,21.33 9.07,15.93 15.93,9.07 21.33,12.75"/>
    </symbol>
  </defs>
</svg>

<main class="app-screen">
  <header class="app-header">
    <h1 class="app-title">Chapel Wave</h1>
    <svg class="menu-toggle" viewBox="0 0 42 42" aria-label="Menu">
      <g stroke="#fff" stroke-width="5" stroke-linecap="round">
        <line x1="3" y1="6" x2="39" y2="6"/>
        <line x1="3" y1="21" x2="39" y2="21"/>
        <line x1="3" y1="36" x2="39" y2="36"/>
      </g>
    </svg>
  </header>

  <nav class="menu-grid">
    <a class="menu-item">
      <svg class="menu-icon" viewBox="0 0 64 64">
        <path d="M14 20c-4 3-5 8-2 14 4 9 11 17 20 21 6 3 10 1 13-2l-7-8-5 3c-6-3-10-8-12-13l3-5-7-8z"/>
        <path d="M30 6h22a5 5 0 0 1 5 5v13a5 5 0 0 1-5 5H42l-7 6v-6h-5a5 5 0 0 1-5-5V11a5 5 0 0 1 5-5z"/>
        <circle cx="35" cy="17.5" r="0.8"/><circle cx="41" cy="17.5" r="0.8"/><circle cx="47" cy="17.5" r="0.8"/>
      </svg>
      <span class="menu-label">Contact Us</span>
    </a>
    <a class="menu-item is-active">
      <svg class="menu-icon" viewBox="0 0 64 64">
        <rect x="6" y="6" width="52" height="38" rx="5"/>
        <path d="M27 16v18l14-9z"/>
        <line x1="6" y1="56" x2="14" y2="56"/>
        <circle cx="19" cy="56" r="3"/>
        <line x1="26" y1="56" x2="58" y2="56"/>
      </svg>
      <span class="menu-label">Video List</span>
    </a>
    <a class="menu-item">
      <svg class="menu-icon" viewBox="0 0 64 64">
        <path d="M6 28v10M14 20v26M22 8v42M30 18v34M38 12v40M46 18v30M54 26v12"/>
        <path d="M6 38a4 4 0 0 0 8 0M14 20a4 4 0 0 1 8 0M22 50a4 4 0 0 0 8 0M30 18a4 4 0 0 1 8 0M38 52a4 4 0 0 0 8 0M46 18a4 4 0 0 1 8 0"/>
      </svg>
      <span class="menu-label">Audio List</span>
    </a>

    <a class="menu-item">
      <svg class="menu-icon" viewBox="0 0 64 64">
        <path d="M44 30V10a4 4 0 0 0-4-4H14a4 4 0 0 0-4 4v44a4 4 0 0 0 4 4h14"/>
        <line x1="18" y1="18" x2="36" y2="18"/><line x1="18" y1="27" x2="36" y2="27"/><line x1="18" y1="36" x2="30" y2="36"/>
        <path d="M34 58l2-8 16-16 6 6-16 16z"/>
        <line x1="48" y1="38" x2="54" y2="44"/>
      </svg>
      <span class="menu-label">Documents<br>List</span>
    </a>
    <a class="menu-item">
      <svg class="menu-icon" viewBox="0 0 64 64">
        <path d="M12 8h40a6 6 0 0 1 6 6v22a6 6 0 0 1-6 6H26l-12 10v-10h-2a6 6 0 0 1-6-6V14a6 6 0 0 1 6-6z"/>
        <line x1="22" y1="21" x2="42" y2="21"/><line x1="22" y1="30" x2="42" y2="30"/>
      </svg>
      <span class="menu-label">Message/<br>Chat Rooms</span>
    </a>
    <a class="menu-item">
      <svg class="menu-icon" viewBox="0 0 64 64">
        <rect x="5" y="5" width="54" height="54" rx="2"/>
        <line x1="5" y1="5" x2="59" y2="59"/>
        <line x1="59" y1="20" x2="32" y2="5"/>
        <path d="M20 52c-5-6-9-11-9-16a9 9 0 0 1 18 0c0 5-4 10-9 16z"/>
        <circle cx="20" cy="36" r="2.5"/>
      </svg>
      <span class="menu-label">Map/<br>Directions</span>
    </a>

    <a class="menu-item">
      <svg class="menu-icon" viewBox="0 0 64 64">
        <rect x="3" y="8" width="58" height="48" rx="3"/>
        <line x1="3" y1="17" x2="61" y2="17"/>
        <circle cx="9" cy="12.5" r="0.6"/><circle cx="14" cy="12.5" r="0.6"/><circle cx="19" cy="12.5" r="0.6"/>
        <rect x="11" y="25" width="5" height="5"/><line x1="23" y1="27.5" x2="53" y2="27.5"/>
        <rect x="11" y="38" width="5" height="5"/><line x1="23" y1="40.5" x2="53" y2="40.5"/>
        <line x1="23" y1="48" x2="53" y2="48"/>
      </svg>
      <span class="menu-label">Webpage</span>
    </a>
    <a class="menu-item">
      <svg class="menu-icon" viewBox="0 0 64 64">
        <use href="#gear"/>
        <circle cx="32" cy="27" r="6"/>
        <path d="M21 44c2-6 6-9 11-9s9 3 11 9"/>
      </svg>
      <span class="menu-label">Profile<br>Settings</span>
    </a>
    <a class="menu-item">
      <svg class="menu-icon" viewBox="0 0 64 64">
        <use href="#gear"/>
        <circle cx="32" cy="32" r="14"/>
        <line x1="32" y1="24" x2="32" y2="34"/>
        <circle cx="32" cy="39.5" r="0.8"/>
      </svg>
      <span class="menu-label">Notification<br>Settings</span>
    </a>

    <a class="menu-item">
      <svg class="menu-icon" viewBox="0 0 64 64">
        <use href="#gear"/>
        <circle cx="32" cy="25" r="6"/>
        <path d="M32 31v16M32 40h4M32 45h4"/>
      </svg>
      <span class="menu-label">Admin<br>Settings</span>
    </a>
    <a class="menu-item">
      <svg class="menu-icon" viewBox="0 0 64 64">
        <circle cx="32" cy="15" r="7"/>
        <circle cx="16" cy="22" r="5"/>
        <circle cx="48" cy="22" r="5"/>
        <path d="M20 52V36a6 6 0 0 1 6-6h12a6 6 0 0 1 6 6v16z"/>
        <path d="M20 36H10a5 5 0 0 0-5 5v11h15M44 36h10a5 5 0 0 1 5 5v11H44"/>
      </svg>
      <span class="menu-label">Manage<br>members</span>
    </a>
    <a class="menu-item">
      <svg class="menu-icon" viewBox="0 0 64 64">
        <path d="M30 58H12a4 4 0 0 1-4-4V10a4 4 0 0 1 4-4h28a4 4 0 0 1 4 4v20"/>
        <line x1="16" y1="18" x2="36" y2="18"/><line x1="16" y1="27" x2="36" y2="27"/><line x1="16" y1="36" x2="26" y2="36"/>
        <circle cx="46" cy="40" r="6"/>
        <path d="M34 58c1-6 6-9 12-9s11 3 12 9z"/>
      </svg>
      <span class="menu-label">View Form<br>Submissions</span>
    </a>
  </nav>
</main>
</body>
</html>
```